Classy business card for accounting firm

We're looking for a new business card for our accounting firm. Our logo was designed by Brandolith, so all of the design info we would like to use has been provided. The specific font provided isn't required to be used.

We want the card to look classy and elegent. Probably more minimalistic, but still with some pops of color.

The options we would like to include on the card are as follows:
1. Main office phone line
2. Direct phone line
3. Email address
4. Website URL
5. Name
6. Title (CEO, President, etc.)
7. Firm Address

The design and card should be double sided!!! The drop down box in the project brief for some reason is defaulting to single sided. Not sure why this is happening.

Thanks!

Contact Information for Business Card

The options we would like to include on the card are as follows: 1. Main office phone line 2. Direct phone line 3. Email address 4. Website URL 5. Name 6. Title (CEO, President, etc.) 7. Firm Address

Requirements
Must have
• Card must be double sided.

```html
<!DOCTYPE html>
<html lang="en">
<head>
<meta charset="utf-8">
<title>Ledgerwell Partners – Business Card</title>
<link rel="stylesheet" href="https://fonts.googleapis.com/css2?family=Montserrat:wght@300;400;500&display=swap">
<style>
  :root {
    --stage: #e6e6e7;
    --paper: #ffffff;
    --ink: #5b5b5d;
    --lime: #b5bd38;
    --orange: #f47d23;
    --white: #ffffff;
  }
  * { box-sizing: border-box; margin: 0; padding: 0; }
  html, body { width: 1200px; height: 1200px; overflow: hidden; }
  body {
    background: var(--stage);
    font-family: "Montserrat", Arial, sans-serif;
    position: relative;
  }
  .card {
    position: absolute;
    left: 150px;
    width: 900px;
    height: 529px;
    background: var(--paper);
    overflow: hidden;
  }
  .card--front { top: 44px; }
  .card--back { top: 619px; }

  .card__shapes { position: absolute; inset: 0; width: 900px; height: 529px; }
  .shape--lime { fill: var(--lime); }
  .shape--orange { fill: var(--orange); }

  /* Brand line on front */
  .brand {
    position: absolute;
    top: 70px;
    left: 220px;
    display: flex;
    align-items: center;
    gap: 22px;
  }
  .brand__mark {
    width: 40px; height: 40px;
    background: var(--orange);
  }
  .brand__text { display: flex; flex-direction: column; align-items: center; }
  .brand__name {
    font-size: 33px;
    font-weight: 500;
    letter-spacing: 1px;
    color: var(--ink);
    line-height: 1;
    white-space: nowrap;
  }
  .tagline {
    display: flex;
    align-items: center;
    gap: 12px;
    font-size: 16px;
    font-weight: 500;
    letter-spacing: 1.6px;
    color: var(--ink);
    margin-top: 10px;
    white-space: nowrap;
  }
  .tagline::before, .tagline::after {
    content: "";
    height: 2px;
    width: 70px;
    background: var(--lime);
  }

  /* Person */
  .person {
    position: absolute;
    left: 62px;
    top: 253px;
    color: var(--white);
  }
  .person__name {
    font-size: 30px;
    font-weight: 500;
    letter-spacing: 1px;
    line-height: 1.15;
    text-transform: uppercase;
  }
  .person__title {
    font-size: 23px;
    font-weight: 400;
    margin-top: 6px;
  }

  /* Contacts */
  .contacts {
    position: absolute;
    right: 130px;
    top: 302px;
    list-style: none;
    color: var(--white);
    font-size: 21px;
    font-weight: 300;
    text-align: right;
  }
  .contacts__item {
    display: flex;
    justify-content: flex-end;
    align-items: center;
    gap: 14px;
    height: 34.5px;
    white-space: nowrap;
  }
  .contacts__item--address { margin-top: 9px; }
  .contacts__icon { width: 20px; height: 20px; flex: none; }
  .contacts__icon * { fill: none; stroke: var(--white); stroke-width: 1.8; stroke-linecap: round; stroke-linejoin: round; }

  /* Back */
  .back__mark {
    position: absolute;
    left: 405px; top: 155px;
    width: 90px; height: 90px;
    background: var(--orange);
  }
  .back__brand {
    position: absolute;
    left: 0; right: 0; top: 308px;
    display: flex; flex-direction: column; align-items: center;
  }
  .back__brand .brand__name { font-size: 48px; letter-spacing: 1.5px; }
  .back__brand .tagline { font-size: 22px; letter-spacing: 2px; margin-top: 14px; gap: 16px; }
  .back__brand .tagline::before, .back__brand .tagline::after { width: 98px; }
</style>
</head>
<body>

<section class="card card--front" aria-label="Business card front">
  <svg class="card__shapes" viewBox="0 0 900 529" aria-hidden="true">
    <polygon class="shape--lime" points="0,156 573,259 0,525"/>
    <polygon class="shape--orange" points="735,181 900,529 100,529"/>
  </svg>

  <div class="brand">
    <div class="brand__mark"></div>
    <div class="brand__text">
      <span class="brand__name">LEDGERWELL PARTNERS</span>
      <span class="tagline">SOLVING TAX PROBLEMS</span>
    </div>
  </div>

  <div class="person">
    <p class="person__name">Daniel<br>Moreton</p>
    <p class="person__title">CEO, President</p>
  </div>

  <ul class="contacts">
    <li class="contacts__item">1234 567 890
      <svg class="contacts__icon" viewBox="0 0 20 20"><path d="M5 3l3 3-2 2c1 2 3 4 5 5l2-2 3 3-2 2C9 16 4 11 3 5z"/><path d="M12 3a5 5 0 0 1 5 5M12 6a2 2 0 0 1 2 2"/></svg>
    </li>
    <li class="contacts__item">1234 567 890
      <svg class="contacts__icon" viewBox="0 0 20 20"><rect x="5" y="1.5" width="10" height="17" rx="2"/><path d="M9 15.5h2"/></svg>
    </li>
    <li class="contacts__item">info@ledgerwell.com.au
      <svg class="contacts__icon" viewBox="0 0 20 20"><rect x="2" y="4.5" width="16" height="11" rx="1"/><path d="M2 5l8 6 8-6"/></svg>
    </li>
    <li class="contacts__item">www.ledgerwell.com.au
      <svg class="contacts__icon" viewBox="0 0 20 20"><circle cx="10" cy="10" r="8"/><path d="M2 10h16M10 2c3 3 3 13 0 16M10 2c-3 3-3 13 0 16"/></svg>
    </li>
    <li class="contacts__item contacts__item--address">42 Wattle Grove Rd Maleny Q 4552
      <svg class="contacts__icon" viewBox="0 0 20 20"><path d="M10 16s-5-5-5-8.5a5 5 0 0 1 10 0C15 11 10 16 10 16z"/><circle cx="10" cy="7.5" r="1.8"/><path d="M4 18.5h12"/></svg>
    </li>
  </ul>
</section>

<section class="card card--back" aria-label="Business card back">
  <div class="back__mark"></div>
  <div class="back__brand">
    <span class="brand__name">LEDGERWELL PARTNERS</span>
    <span class="tagline">SOLVING TAX PROBLEMS</span>
  </div>
</section>

</body>
</html>
```